New professional looking flyer for company

I need our flyer updated my flyer is the Lvb flyer Have attached current flyer so you know what services need to be listed. Want it to be in mainly dark colours like black and dark grey with pops of light grey, silver or white. i have added several photos for you to choose which ones work best with your design would like The photos to be in colour for the flyer. But can have a mix of greyscale if that works for your design j have attached another companies flyers as design ideas to show what I am looking for

Target Market(s)

new clients

Industry/Entity Type

transport and earthmoving

Colors

Designer to choose colors to be used in the design.

Requirements
Nice to have
• Look professional
Should not have
• No orange or red or green

```html
<!DOCTYPE html>
<html lang="en">
<head>
<meta charset="utf-8">
<title>Lvb Pty Ltd – Our Services</title>
<link href="https://fonts.googleapis.com/css2?family=Teko:wght@500;600&family=Montserrat:wght@400&display=swap" rel="stylesheet">
<style>
  :root {
    --page-bg: #8d8d8f;
    --ink-black: #050505;
    --deep-grey: #1d1b1c;
    --mid-grey: #5a5a5c;
    --silver: #c9c9cb;
    --panel-white: #f3f3f3;
    --band-grey: #d6d6d6;
    --text-dark: #1f1c1d;
    --gold: #b8862f;
    --footer-grey: #3a3a3b;
  }
  * { margin: 0; padding: 0; box-sizing: border-box; }
  html, body { width: 1001px; height: 1200px; overflow: hidden; background: var(--page-bg); }
  .flyer {
    position: absolute; left: 36px; top: 0; width: 928px; height: 1200px; overflow: hidden;
    background: radial-gradient(ellipse 420px 300px at 50% 22%, #3a3a3c 0%, #151515 60%, var(--ink-black) 100%);
    font-family: "Teko", sans-serif;
  }
  .brand { position: absolute; top: 58px; left: 0; width: 100%; text-align: center; }
  .brand-name {
    font-family: "Teko", sans-serif; font-weight: 600; font-size: 150px; line-height: 110px;
    color: var(--silver); letter-spacing: 4px;
  }
  .brand-suffix {
    font-family: "Teko", sans-serif; font-weight: 600; font-size: 34px; line-height: 34px;
    color: var(--mid-grey); margin-top: 10px;
  }
  .photo { position: absolute; }
  .photo-top {
    left: 0; top: 292px; width: 928px; height: 190px;
    background: linear-gradient(90deg, #2b2b2c 0%, #4a4a4b 40%, #3a3a3b 62%, #7a5038 80%, #d8d4cc 100%);
    opacity: .9;
  }
  .photo-bottom-left {
    left: 0; top: 895px; width: 430px; height: 220px;
    background: linear-gradient(90deg, #8a7a3e 0%, #5c4a35 35%, #2a2724 65%, #8b8682 100%);
    border-radius: 6px 6px 0 0;
  }
  .photo-bottom-right {
    left: 562px; top: 890px; width: 366px; height: 230px;
    background: linear-gradient(90deg, #c2b58e 0%, #2a2826 35%, #9c9896 60%, #e9e9ea 100%);
    border-radius: 6px 0 0 0;
  }
  .services {
    position: absolute; left: 66px; top: 482px; width: 800px; height: 448px;
    background: var(--panel-white); border-radius: 14px;
  }
  .services-tab {
    position: absolute; left: 250px; top: 460px; width: 426px; height: 58px;
    background: var(--deep-grey); border-radius: 0 0 30px 30px;
    color: #f2f2f2; font-weight: 600; font-size: 48px; line-height: 68px;
    text-align: center; letter-spacing: 1px;
  }
  .service-list { position: absolute; list-style: none; }
  .service-list.left { left: 84px; top: 548px; width: 420px; }
  .service-list.right { left: 511px; top: 548px; width: 340px; }
  .service-item {
    height: 44.6px; display: flex; align-items: center; gap: 9px;
    font-weight: 500; font-size: 31px; color: var(--text-dark); padding-left: 6px;
  }
  .service-item.banded { background: linear-gradient(90deg, var(--band-grey), rgba(214,214,214,0)); }
  .service-item .tick { width: 24px; height: 24px; flex: none; }
  .service-item.no-tick { padding-left: 39px; }
  .service-item span { padding-top: 6px; }
  .callout { position: absolute; left: 66px; top: 830px; width: 800px; text-align: center; font-weight: 600; font-size: 25px; line-height: 27px; }
  .callout .line-one { color: var(--text-dark); }
  .callout .line-two { color: var(--gold); }
  .footer {
    position: absolute; left: 0; top: 1090px; width: 928px; height: 110px;
    background: linear-gradient(180deg, #5a5a5b 0%, var(--footer-grey) 45%, #111 100%);
    border-top: 3px solid #e6e6e6;
  }
  .phone-icon { position: absolute; left: 54px; top: 1130px; width: 46px; height: 50px; }
  .phone-number {
    position: absolute; left: 125px; top: 1116px; font-weight: 600; font-size: 72px; line-height: 72px;
    color: #d9d9d9; letter-spacing: 1px;
  }
  .contact { position: absolute; left: 490px; top: 1137px; font-family: "Montserrat", sans-serif; font-size: 15px; line-height: 21px; color: #f2f2f2; }
  .contact-row { display: flex; align-items: center; gap: 12px; }
  .contact-row svg { width: 13px; height: 13px; flex: none; }
</style>
</head>
<body>
<div class="flyer">
  <div class="photo photo-top" role="img" aria-label="Greyscale photo of side-tipper road trains on a dirt yard with a white skid steer loader pushing red earth"></div>

  <header class="brand">
    <div class="brand-name">LVB</div>
    <div class="brand-suffix">Pty Ltd</div>
  </header>

  <section class="services"></section>
  <div class="services-tab">OUR SERVICES</div>

  <ul class="service-list left">
    <li class="service-item banded"><svg class="tick" viewBox="0 0 24 24"><circle cx="12" cy="12" r="10" fill="none" stroke="#555" stroke-width="1.6"/><path d="M7 12l4 4 8-9" fill="none" stroke="#b8862f" stroke-width="2"/></svg><span>Over size loads / Hot Shot Loads</span></li>
    <li class="service-item"><svg class="tick" viewBox="0 0 24 24"><circle cx="12" cy="12" r="10" fill="none" stroke="#555" stroke-width="1.6"/><path d="M7 12l4 4 8-9" fill="none" stroke="#b8862f" stroke-width="2"/></svg><span>Heavy Vehicle Recovery services</span></li>
    <li class="service-item banded"><svg class="tick" viewBox="0 0 24 24"><circle cx="12" cy="12" r="10" fill="none" stroke="#555" stroke-width="1.6"/><path d="M7 12l4 4 8-9" fill="none" stroke="#b8862f" stroke-width="2"/></svg><span>Potable Water Deliveries</span></li>
    <li class="service-item"><svg class="tick" viewBox="0 0 24 24"><circle cx="12" cy="12" r="10" fill="none" stroke="#555" stroke-width="1.6"/><path d="M7 12l4 4 8-9" fill="none" stroke="#b8862f" stroke-width="2"/></svg><span>Road Building / Maintenance</span></li>
    <li class="service-item banded"><svg class="tick" viewBox="0 0 24 24"><circle cx="12" cy="12" r="10" fill="none" stroke="#555" stroke-width="1.6"/><path d="M7 12l4 4 8-9" fill="none" stroke="#b8862f" stroke-width="2"/></svg><span>Earthworks</span></li>
    <li class="service-item"><svg class="tick" viewBox="0 0 24 24"><circle cx="12" cy="12" r="10" fill="none" stroke="#555" stroke-width="1.6"/><path d="M7 12l4 4 8-9" fill="none" stroke="#b8862f" stroke-width="2"/></svg><span>Sand &amp; Metal Supply &amp; Cartage</span></li>
  </ul>

  <ul class="service-list right">
    <li class="service-item banded"><svg class="tick" viewBox="0 0 24 24"><circle cx="12" cy="12" r="10" fill="none" stroke="#555" stroke-width="1.6"/><path d="M7 12l4 4 8-9" fill="none" stroke="#b8862f" stroke-width="2"/></svg><span>Road Train Tippers</span></li>
    <li class="service-item"><svg class="tick" viewBox="0 0 24 24"><circle cx="12" cy="12" r="10" fill="none" stroke="#555" stroke-width="1.6"/><path d="M7 12l4 4 8-9" fill="none" stroke="#b8862f" stroke-width="2"/></svg><span>Road Train Tankers</span></li>
    <li class="service-item banded"><svg class="tick" viewBox="0 0 24 24"><circle cx="12" cy="12" r="10" fill="none" stroke="#555" stroke-width="1.6"/><path d="M7 12l4 4 8-9" fill="none" stroke="#b8862f" stroke-width="2"/></svg><span>Road Train Flat Tops</span></li>
    <li class="service-item"><svg class="tick" viewBox="0 0 24 24"><circle cx="12" cy="12" r="10" fill="none" stroke="#555" stroke-width="1.6"/><path d="M7 12l4 4 8-9" fill="none" stroke="#b8862f" stroke-width="2"/></svg><span>Drop Deck Trailers</span></li>
    <li class="service-item banded"><svg class="tick" viewBox="0 0 24 24"><circle cx="12" cy="12" r="10" fill="none" stroke="#555" stroke-width="1.6"/><path d="M7 12l4 4 8-9" fill="none" stroke="#b8862f" stroke-width="2"/></svg><span>Mine site accredited</span></li>
    <li class="service-item no-tick"><span>Equipment &amp; Operators</span></li>
  </ul>

  <div class="callout">
    <div class="line-one">WE OFFER A LARGE RANGE OF SERVICES NOT LISTED SO CALL US TODAY</div>
    <div class="line-two">FOR A PERSONALISED QUOTE TO SUIT YOUR NEEDS.</div>
  </div>

  <div class="photo photo-bottom-left" role="img" aria-label="Colour photo of a black prime mover with bull bar hauling a yellow grader on a low loader"></div>
  <div class="photo photo-bottom-right" role="img" aria-label="Colour photo of two road train prime movers, one black and one white, with chrome bull bars"></div>

  <footer class="footer"></footer>
  <svg class="phone-icon" viewBox="0 0 46 50"><rect x="14" y="2" width="22" height="42" rx="4" fill="none" stroke="#e6e6e6" stroke-width="3"/><line x1="21" y1="38" x2="29" y2="38" stroke="#e6e6e6" stroke-width="2"/><path d="M14 18c-6 2-10 8-10 14 0 6 4 10 10 12z" fill="#e6e6e6"/><path d="M38 14h4M38 22h4M38 30h4" stroke="#e6e6e6" stroke-width="3"/></svg>
  <div class="phone-number">041 555 2718</div>
  <div class="contact">
    <div class="contact-row"><svg viewBox="0 0 14 14"><path d="M7 1a4 4 0 0 1 4 4c0 3-4 8-4 8S3 8 3 5a4 4 0 0 1 4-4z" fill="#b8862f"/><circle cx="7" cy="5" r="1.5" fill="#3a3a3b"/></svg><span>Depot: Lot 46, Ridgeback Track Marrow Flats</span></div>
    <div class="contact-row"><svg viewBox="0 0 14 14"><rect x="1" y="3" width="12" height="8" fill="#b8862f"/><path d="M1 3l6 5 6-5" fill="none" stroke="#3a3a3b" stroke-width="1"/></svg><span>accounts@lvbhaulage.com.au</span></div>
  </div>
</div>
</body>
</html>
```